Artistic Poster for a Short Film

I am the Writer/Director of an upcoming short film called "Driftwater" and I need a 20x30 poster for the project screening. The screening is coming up very soon so apologies for the quick turnaround time. Here is a short synopsis:

"Owen is a mysterious man who is lost and disoriented. With the help of Marisol, he searches for items out of an old diary written long ago by a woman named Greta, despite not understanding exactly why he does so. Marisol helps, but when they are unsuccessful she confronts Owen: Does he know why he restlessly searches for these items? The truth is shocking, and reveals Owen's connections to Marisol, Greta, and the strange old diary.

The truth is that Owen is actually an old man, and Marisol is his caretaker and granddaughter. His memories, including those of Greta, his deceased wife, have been destroyed by Dementia. He often wakes believing himself to be at an earlier stage of his life, and therefore meets many of the challenges of life with anger and confusion."

Here is the film's website: http://www.driftwater-film.example
Here is our successful Fundhive: http://www.fundhive.example/projects/482617305/driftwater-a-short-film

The design should be dark and simple. I'm a fan of the art-prints that this short film used (scroll down to see): http://www.fundhive.example/projects/marcuvolden/ember-a-short-film-based-on-the-story-by-lydia-crane but I'm also open to other ideas. If you google "alternative movie posters" you'll see what I mean. The poster should be simple, easy to read, and hint at the themes of the film without giving the twist away.

Here is a link to the Fine Cut of the film: https://clipvault.example/51204977 The password is: lanterns47
It is not a completed version but will give you an idea of what the film will look like.

Target Market(s)

The intended audience is an art-film crowd of moviegoers.

Industry/Entity Type

Movie

Requirements
Must have
• The poster must have the typical movie poster text at the bottom. The information that should be included is: First line: HOLLOW BIRCH PRODUCTIONS presents a film by DANIEL OKAFOR "DRIFTWATER" MATTHIEU LAVERNE TORI BALSDEN
Second line: music by OLAF BRISK director of photography CALVIN R. OSTROM edited by ELIAS VOSS costume designer JOSELYNE TARRAW
Third line: produced by IVY KOWALCZE DANIEL OKAFOR written and directed by DANIEL OKAFOR

It should have the title of the film "Driftwater" and "A film by Daniel Okafor" on the poster (in addition to the text at the bottom.

It must be high-quality and printable to a size of 20x30. Ideal resolution is 6060x9090. I only need the high quality printable file, I will do the printing myself.
Should not have
• Bright colors.

```html
<!DOCTYPE html>
<html lang="en">
<head>
<meta charset="utf-8">
<title>Driftwater — Poster</title>
<link rel="stylesheet" href="https://fonts.googleapis.com/css2?family=Cinzel:wght@400&family=Oswald:wght@300;400&display=swap">
<style>
  :root {
    --paper: #efe9d8;
    --ink-navy: #1a2233;
    --ink-navy-deep: #0e1421;
    --ink-navy-soft: #273248;
    --figure-tone: rgba(214, 207, 192, 0.78);
    --figure-mid: rgba(170, 164, 152, 0.38);
    --bench-tone: rgba(200, 194, 180, 0.32);
    --title-white: #ebe8e1;
    --credit-grey: #c9c7c2;
  }
  * { box-sizing: border-box; margin: 0; padding: 0; }
  html, body {
    width: 920px;
    height: 1200px;
    overflow: hidden;
    background: var(--paper);
  }
  .poster {
    position: relative;
    width: 920px;
    height: 1200px;
    background: var(--paper);
    padding: 30px;
  }
  .poster__field {
    position: relative;
    width: 100%;
    height: 100%;
    background:
      radial-gradient(ellipse 70% 55% at 50% 38%, var(--ink-navy-soft) 0%, var(--ink-navy) 60%, var(--ink-navy-deep) 100%);
    overflow: hidden;
  }

  /* Artwork area: soft tonal placeholder for the two seated figures on a bench */
  .artwork {
    position: absolute;
    left: 0;
    top: 100px;
    width: 860px;
    height: 620px;
  }
  .artwork__glow {
    position: absolute;
    border-radius: 50%;
  }
  .artwork__glow--left {
    left: 70px;
    top: 20px;
    width: 360px;
    height: 560px;
    background: radial-gradient(closest-side, var(--figure-tone) 0%, var(--figure-mid) 55%, transparent 100%);
  }
  .artwork__glow--right {
    left: 470px;
    top: 20px;
    width: 360px;
    height: 580px;
    background: radial-gradient(closest-side, var(--figure-tone) 0%, var(--figure-mid) 55%, transparent 100%);
  }
  .artwork__glow--bench {
    left: 300px;
    top: 230px;
    width: 560px;
    height: 160px;
    background: radial-gradient(closest-side, var(--bench-tone) 0%, transparent 100%);
  }

  .poster__title {
    position: absolute;
    left: 0;
    right: 0;
    top: 808px;
    text-align: center;
    font-family: "Cinzel", "Trajan Pro", serif;
    font-weight: 400;
    font-size: 80px;
    letter-spacing: 4px;
    color: var(--title-white);
    line-height: 1;
  }
  .poster__byline {
    position: absolute;
    left: 0;
    right: 0;
    top: 918px;
    text-align: center;
    font-family: "Cinzel", serif;
    font-size: 14px;
    letter-spacing: 7px;
    color: var(--title-white);
  }
  .credits {
    position: absolute;
    left: 0;
    right: 0;
    top: 1000px;
    display: flex;
    flex-direction: column;
    align-items: center;
    gap: 12px;
    font-family: "Oswald", "Arial Narrow", sans-serif;
    font-weight: 300;
    color: var(--credit-grey);
    text-transform: uppercase;
  }
  .credits__line {
    display: flex;
    align-items: center;
    gap: 7px;
    font-size: 21px;
    line-height: 1;
    letter-spacing: 0.3px;
    white-space: nowrap;
  }
  .credits__role {
    display: inline-flex;
    flex-direction: column;
    font-size: 7px;
    line-height: 1.05;
    letter-spacing: 0.4px;
    text-align: right;
    color: var(--credit-grey);
  }
</style>
</head>
<body>
  <main class="poster">
    <div class="poster__field">
      <div class="artwork" role="img"
           aria-label="Weathered ink-wash illustration of two elderly men seated apart on a park bench, pale figures against the dark field">
        <span class="artwork__glow artwork__glow--bench" aria-hidden="true"></span>
        <span class="artwork__glow artwork__glow--left" aria-hidden="true"></span>
        <span class="artwork__glow artwork__glow--right" aria-hidden="true"></span>
      </div>

      <h1 class="poster__title">DRIFTWATER</h1>
      <p class="poster__byline">A FILM BY DANIEL OKAFOR</p>

      <section class="credits">
        <p class="credits__line">
          <span>HOLLOW BIRCH PRODUCTIONS</span>
          <span class="credits__role"><span>presents</span><span>a film by</span></span>
          <span>DANIEL OKAFOR "DRIFTWATER" MATTHIEU LAVERNE TORI BALSDEN</span>
        </p>
        <p class="credits__line">
          <span class="credits__role"><span>music</span><span>by</span></span>
          <span>OLAF BRISK</span>
          <span class="credits__role"><span>director of</span><span>photography</span></span>
          <span>CALVIN R. OSTROM</span>
          <span class="credits__role"><span>edited</span><span>by</span></span>
          <span>ELIAS VOSS</span>
          <span class="credits__role"><span>costume</span><span>designer</span></span>
          <span>JOSELYNE TARRAW</span>
        </p>
        <p class="credits__line">
          <span class="credits__role"><span>produced</span><span>by</span></span>
          <span>IVY KOWALCZE DANIEL OKAFOR</span>
          <span class="credits__role"><span>written</span><span>by</span></span>
          <span>DANIEL OKAFOR</span>
          <span class="credits__role"><span>directed</span><span>by</span></span>
          <span>DANIEL OKAFOR</span>
        </p>
      </section>
    </div>
  </main>
</body>
</html>
```